Pediatric Vision Care: Myopia Control Brochure

We are a pediatric eye care practice (ophthalmology and optometry). One of our services we offer for children is myopia control, which are strategies for slowing or stopping the progression of nearsightedness. This is a service we need to sell to parents because most insurance won't pay for it. There are different options we offer that can work well for kids in different situations: glasses with Durovant lenses, atropine eye drops, and/or special contact lenses. We need a brochure we can distribute to parents to let them know about this service that would encourage them to buy it for children who need it. Attached is our initial draft brochure created by our staff that provides text that we want to keep. The images and layout can change. We probably need at least one or two photos of kids on the brochure, because this is only something that works for children who are still growing, and the target audience is parents of 4-8 year old children.

Target Market(s)

Parents of 4-8 year old children

Font styles to use
Sans Serif

Requirements
Must have
• I'm uploading our company logo that should be included somewhere on the brochure. You can include contact information (web address, phone number) for our practice that is found on our website: http://www.maplebrookkidsvision.com/
Should not have
• This should not look childish. We need the impression to be friendly but professional, medical, expert.

```html
<!DOCTYPE html>
<html lang="en">
<head>
<meta charset="utf-8">
<title>Myopia Control Brochure</title>
<link href="https://fonts.googleapis.com/css2?family=Poppins:wght@300;400;500;600&display=swap" rel="stylesheet">
<style>
:root{
  --navy:#1c3461;
  --green:#a9cf86;
  --purple:#cbc3e3;
  --lavender:#e4e0f0;
  --peach:#f5dcc3;
  --yellow:#f6e79f;
  --orange:#f26b21;
  --grey:#f3f3f3;
  --text:#5a5a5a;
  --stage:#e9e7e8;
}
*{box-sizing:border-box;margin:0;padding:0}
html,body{width:887px;height:1200px;overflow:hidden}
body{background:var(--stage);font-family:'Poppins',sans-serif;color:var(--text);position:relative}
.sheet{position:absolute;left:68px;width:750px;height:580px;background:#fff;box-shadow:0 2px 8px rgba(0,0,0,.12);overflow:hidden}
.sheet-outside{top:10px}
.sheet-inside{top:610px}
.block{position:absolute}
.photo{position:absolute}
h2.panel-title{font-weight:500;color:var(--navy);font-size:16px;line-height:20px}
.rule{position:absolute;height:0;border-top:1.5px dotted var(--orange)}
p.body{font-size:9.6px;line-height:11.8px;font-weight:300;color:var(--text)}
p.body + p.body{margin-top:11px}
.justify{text-align:justify}
.band{position:absolute;display:flex;align-items:center;justify-content:center;font-size:12.5px;letter-spacing:4px;color:#2e3a2a;font-weight:500}
.footer{position:absolute;left:0;bottom:0;width:750px;height:36px;background:var(--navy);border-top:2px solid var(--orange);display:flex;align-items:center;justify-content:center;color:#fff;font-size:9.5px;font-weight:600;letter-spacing:.3px}
.brand{display:flex;align-items:center;gap:7px;color:var(--navy);font-weight:500;white-space:nowrap}
.brand .dot{border-radius:50%;background:var(--orange);flex:none}
.contact-line{font-size:9.5px;font-weight:300;color:var(--text);text-align:center;line-height:12px}
.contact-line b{font-weight:600;color:#333}
.icon{display:block;margin:0 auto 4px}
.option-head{position:absolute;top:0;height:81px;display:flex;align-items:center;padding-left:32px;font-size:16.5px;line-height:20px;color:var(--navy);font-weight:400}
.option-text{position:absolute;top:122px;width:195px}
.option-text b{font-weight:600;color:#333}
.stars{color:var(--orange);font-size:17px;letter-spacing:3px;text-align:center}
.quote{font-size:9.6px;line-height:11.8px;color:#444;font-weight:300;margin-top:8px}
.quote b{font-weight:600;color:var(--navy)}
</style>
</head>
<body>

<section class="sheet sheet-outside">
  <div class="block" style="left:27px;top:32px;width:200px">
    <h2 class="panel-title">Healty Lifestyle Habits</h2>
  </div>
  <div class="rule" style="left:27px;top:65px;width:124px"></div>
  <div class="block" style="left:24px;top:82px;width:198px">
    <p class="body">Too much screen time and prolonged near work, especially at very close distances, may worsen nearsightedness. We recommend limiting non-academic screen use and following:</p>
    <p class="body justify">Healthy daily habits can help slow myopia progression. Studies show children who spend at least 2 hours outdoors daily are less likely to develop myopia and may experience slower progression.</p>
  </div>
  <div class="band" style="left:0;top:247px;width:249px;height:35px;background:var(--green)">THE 20-20-20 RULE</div>
  <div class="block" style="left:27px;top:300px;width:210px;display:flex;gap:12px;align-items:flex-start">
    <svg width="32" height="32" viewBox="0 0 32 32" aria-hidden="true"><circle cx="16" cy="16" r="16" fill="var(--navy)"/><path d="M6 16c3-5 7-7 10-7s7 2 10 7c-3 5-7 7-10 7s-7-2-10-7z" fill="none" stroke="#fff" stroke-width="1.8"/><circle cx="16" cy="16" r="3.4" fill="none" stroke="#fff" stroke-width="1.8"/></svg>
    <p class="body" style="margin-top:0">Every 20 minutes, take a 20-second break and look at something at least 20 ft away.</p>
  </div>
  <div class="photo" role="img" aria-label="Photo of a young girl in glasses playing with a ball outdoors in a garden" style="left:0;top:357px;width:249px;height:187px;background:linear-gradient(135deg,#b7c79b,#7d9a63 55%,#9fb885)"></div>

  <div class="block" style="left:249px;top:30px;width:248px;text-align:center">
    <h2 class="panel-title">Expert Care<br>For Children Vision</h2>
  </div>
  <div class="rule" style="left:327px;top:78px;width:126px"></div>
  <div class="photo" role="img" aria-label="Photo of the bright clinic reception area with a wooden front desk" style="left:251px;top:99px;width:246px;height:148px;background:linear-gradient(180deg,#e8eaec,#cfd3d6 60%,#b9a58c)"></div>
  <div class="band" style="left:251px;top:247px;width:246px;height:35px;background:var(--purple)">CONTACT</div>
  <div class="block" style="left:251px;top:282px;width:246px;height:262px;background:var(--grey)">
    <div class="brand" style="justify-content:center;margin-top:30px;font-size:11.5px"><span class="dot" style="width:9px;height:9px"></span>Maplebrook Kids Vision</div>
    <div style="margin-top:22px">
      <svg class="icon" width="12" height="12" viewBox="0 0 12 12" aria-hidden="true"><circle cx="6" cy="6" r="5.4" fill="none" stroke="#9a8fc4" stroke-width=".8"/><path d="M4 3.5l1 1-.6.8c.4.8 1 1.4 1.8 1.8l.8-.6 1 1-.7.9c-2 0-4-2-4-4z" fill="#9a8fc4"/></svg>
      <div class="contact-line"><b>Voice:</b> (555) 214-0187</div>
    </div>
    <div style="margin-top:10px">
      <svg class="icon" width="12" height="12" viewBox="0 0 12 12" aria-hidden="true"><circle cx="6" cy="6" r="5.4" fill="none" stroke="#9a8fc4" stroke-width=".8"/><path d="M4 3.5l1 1-.6.8c.4.8 1 1.4 1.8 1.8l.8-.6 1 1-.7.9c-2 0-4-2-4-4z" fill="#9a8fc4"/></svg>
      <div class="contact-line"><b>Text:</b> (555) 214-0192</div>
    </div>
    <div style="margin-top:10px">
      <svg class="icon" width="12" height="12" viewBox="0 0 12 12" aria-hidden="true"><circle cx="6" cy="6" r="5.4" fill="none" stroke="#9a8fc4" stroke-width=".8"/><rect x="3.3" y="4" width="5.4" height="4" fill="none" stroke="#9a8fc4" stroke-width=".8"/><path d="M3.3 4l2.7 2 2.7-2" fill="none" stroke="#9a8fc4" stroke-width=".8"/></svg>
      <div class="contact-line">appointments@maplebrookkidsvision.com</div>
    </div>
    <div style="margin-top:10px">
      <svg class="icon" width="12" height="12" viewBox="0 0 12 12" aria-hidden="true"><circle cx="6" cy="6" r="5.4" fill="none" stroke="#9a8fc4" stroke-width=".8"/><path d="M6 9.2C4.6 7.6 4 6.6 4 5.4a2 2 0 014 0c0 1.2-.6 2.2-2 3.8z" fill="none" stroke="#9a8fc4" stroke-width=".8"/></svg>
      <div class="contact-line">Maplebrook Kids Vision<br>1280 Harbor Lane<br>Maplebrook, VA 23999</div>
    </div>
  </div>

  <div class="brand" style="position:absolute;left:555px;top:48px;font-size:14px"><span class="dot" style="width:12px;height:12px"></span>Maplebrook Kids Vision</div>
  <div class="photo" role="img" aria-label="Photo of a smiling girl covering one eye in front of an eye chart" style="left:497px;top:92px;width:253px;height:190px;background:linear-gradient(180deg,#f4f4f4,#e6dfd8 55%,#d9b896)"></div>
  <div class="block" style="left:497px;top:282px;width:253px;height:74px;background:var(--peach);display:flex;align-items:center;justify-content:center">
    <h1 style="font-size:21px;font-weight:500;color:var(--navy);letter-spacing:.3px">MYOPIA CONTROL</h1>
  </div>
  <div class="block" style="left:521px;top:378px;width:200px">
    <p class="body justify">helps slow eye growth, keep glasses prescriptions lower, and reduce the risk of eye disease in adulthood.</p>
  </div>
  <div class="rule" style="left:521px;top:430px;width:200px"></div>
  <div class="block" style="left:521px;top:443px;width:200px">
    <p class="body justify">Myopia causes blurry distance vision because the eye elongates and usually worsens throughout childhood. It is becoming increasingly common. Higher myopia &amp; stronger glasses prescriptions increase the risk of retinal problems and macular degeneration in adulthood.</p>
  </div>

  <footer class="footer">WWW.MAPLEBROOKKIDSVISION.COM</footer>
</section>

<section class="sheet sheet-inside">
  <div class="option-head" style="left:0;width:249px;background:var(--green);color:#3b4a33">Lumora Durovant<br>glasses lenses</div>
  <div class="option-head" style="left:249px;width:241px;background:var(--peach);padding-left:40px">Low-dose<br>Atropine</div>
  <div class="option-head" style="left:490px;width:260px;background:var(--yellow);padding-left:38px;color:#4a4420">Specialty<br>Contact Lenses</div>

  <div class="option-text" style="left:30px;top:118px">
    <p class="body">FDA market authorized Lumora Durovant glasses lenses have been shown to <b>slow myopia progression by about 50% in children aged 6–12.</b></p>
    <p class="body">These lenses are a great treatment option because all your child needs to do is wear glasses. They look almost identical to ordinary glasses, but use specialized optics to signal the brain to slow the growth of myopic eyes.</p>
  </div>
  <div class="option-text" style="left:276px;top:118px;width:200px">
    <p class="body">These eyedrops have been studied for over 20 years and have been shown to <b>slow myopia progression by about 50% when used consistently.</b></p>
    <p class="body">Low-dose atropine is simple to add to your daily routine. One drop is placed in each eye before bed each evening. These are ordered from a compounding pharmacy and mailed directly to your home.</p>
  </div>
  <div class="option-text" style="left:525px;top:122px;width:200px">
    <p class="body">FDA-approved ClearPath lenses have been shown to <b>slow myopia progression by about 50% in children aged 8–12.</b></p>
    <p class="body">Contact lenses can be a great fit for many children, especially active children or those who do not enjoy wearing glasses. Many children as young as 7 or 8 are successful at wearing contacts</p>
  </div>

  <div class="photo" role="img" aria-label="Close-up image of an eyeglass lens showing concentric ring optics" style="left:0;top:282px;width:249px;height:128px;background:linear-gradient(135deg,#aec3c6,#7e9ea4 60%,#c5d3d3)"></div>
  <div class="photo" role="img" aria-label="Photo of a doctor examining a young girl's eyes in the clinic" style="left:251px;top:282px;width:245px;height:128px;background:linear-gradient(135deg,#f1f1f1,#d8d8d8 55%,#c98f78)"></div>
  <div class="photo" role="img" aria-label="Photo of a smiling boy pointing to his eye" style="left:498px;top:282px;width:252px;height:128px;background:linear-gradient(135deg,#f6f6f6,#e9ddd2 55%,#d4b199)"></div>

  <div class="block" style="left:0;top:410px;width:249px;height:134px;display:flex;align-items:center;justify-content:center">
    <div class="brand" style="font-size:14px"><span class="dot" style="width:12px;height:12px"></span>Maplebrook Kids Vision</div>
  </div>
  <div class="block" style="left:249px;top:410px;width:501px;height:134px;background:var(--lavender);padding:22px 27px 0 27px">
    <div class="stars">★★★★★</div>
    <p class="quote">Everyone a Maplebrook Kids Vision was very nice and accommodating. They made us feel comfortable as soon as we walked in the door. Dr. Helen Marsh was professional, yet had a warm personality and was great with my 2 yr old daughter and explained everything so we could easily understand it. Our entire experience there with everyone was just great. I highly recommend this practice - <b>Dana Whitfield</b></p>
  </div>

  <footer class="footer">WWW.MAPLEBROOKKIDSVISION.COM</footer>
</section>

</body>
</html>
```